Wordpress web design

We need a website buil in using Wordpress with 5 pages.

Pages: HOME SERVICES GALLERY TESTIMONIALS CONTACT US ABOUT US.

We are looking for a unique, professional and clean web for our construction company.

Company name: TALL OAK BUILDING SERVICES. We can olso provide you with the logo. Please don't use any flashin, intro, or any ready templates.

All your ideas are welcome.

Many thanks,
Dorian

Target Market(s)

Construction

Industry/Entity Type

Construction

Font styles to use
Sans Serif
Decorative

Requirements
Must have
• Connect with construction and London
Nice to have
• Nice and clean

```html
<!DOCTYPE html>
<html lang="en">
<head>
<meta charset="utf-8">
<title>Tall Oak Building Services</title>
<link href="https://fonts.googleapis.com/css2?family=Open+Sans:wght@400;600;700&family=Raleway:wght@400;600;700&display=swap" rel="stylesheet">
<style>
:root{
  --red:#d7212b;
  --blue:#2a8fd8;
  --ink:#333;
  --muted:#777;
  --light:#f1f1f1;
  --line:#dcdcdc;
  --footer:#2f3438;
  --footer-deep:#23272a;
  --white:#fff;
}
*{box-sizing:border-box;margin:0;padding:0}
html,body{width:1200px;height:2500px;overflow:hidden;background:var(--white)}
body{font-family:"Open Sans",Arial,sans-serif;color:var(--ink);font-size:13px;line-height:1.55;position:relative}
.wrap{width:1040px;margin:0 auto;position:relative}

/* header */
.topbar{height:92px}
.brand{position:absolute;left:0;top:22px;display:flex;align-items:center;gap:10px}
.brand-mark{width:40px;height:40px;background:var(--red)}
.brand-name{font-family:"Raleway",sans-serif;font-weight:700;font-size:17px;color:var(--ink);line-height:1.1;width:150px}
.contact{position:absolute;right:0;top:26px;font-size:12px;color:var(--ink)}
.contact div{display:flex;align-items:center;gap:8px;margin-bottom:6px}
.contact svg{width:13px;height:13px}
.nav{background:var(--red);height:40px}
.nav ul{list-style:none;display:flex;height:40px;align-items:center}
.nav li{color:var(--white);font-weight:700;font-size:12px;padding:0 14px;height:40px;line-height:40px}
.nav li.active{background:#b0151e}
.nav .search{position:absolute;right:10px;top:12px;width:16px;height:16px}

/* hero */
.hero{height:670px;position:relative;background:linear-gradient(180deg,#8fa7b9 0%,#b8b4a6 35%,#8c8470 60%,#4d5e33 85%,#3b4a2a 100%)}
.hero-quote{position:absolute;left:140px;top:420px;color:var(--white);font-family:"Raleway",sans-serif}
.hero-quote h1{font-size:40px;font-weight:700;line-height:1.2}
.hero-quote p{text-align:right;font-style:italic;font-size:16px;margin-top:6px}
.hero .arrow{position:absolute;top:320px;width:28px;height:28px}
.hero .prev{left:20px}.hero .next{right:20px}
.dots{position:absolute;left:50%;transform:translateX(-50%);bottom:30px;display:flex;gap:8px}
.dots span{width:9px;height:9px;border-radius:50%;background:rgba(255,255,255,.6)}
.dots span.on{background:var(--white)}

/* section heads */
.sec-title{font-family:"Raleway",sans-serif;font-size:26px;text-align:center;color:var(--blue);font-weight:400}
.sec-title em{font-style:normal;color:var(--red)}
.services-head{margin-top:36px;display:flex;justify-content:center;align-items:center;gap:24px}
.services-head svg{width:16px;height:16px}

/* service cards */
.cards{display:flex;gap:28px;margin-top:28px}
.card{flex:1;background:var(--light);padding:20px 0 16px;position:relative;height:480px}
.card h3{font-family:"Raleway",sans-serif;font-size:24px;font-weight:400;color:var(--blue);padding:0 20px 16px}
.card h3 em{font-style:normal;color:var(--red)}
.card .photo{height:170px}
.card p{padding:18px 20px;font-size:12px;color:var(--ink)}
.more{position:absolute;right:18px;bottom:16px;background:var(--red);color:var(--white);font-size:10px;font-weight:700;padding:3px 10px}

/* about */
.about{margin-top:38px;text-align:center}
.about p{margin-top:14px;font-size:12px;padding:0 40px}
.rule{border:0;border-top:1px solid var(--line);margin-top:30px}

/* gallery */
.gallery{margin-top:24px}
.gallery-row{display:flex;gap:12px;margin-top:24px}
.gallery-row div{flex:1;height:170px}

/* testimonials */
.testimonials{margin-top:44px}
.testimonials h2{font-family:"Raleway",sans-serif;font-size:26px;font-weight:400;color:var(--blue);display:flex;align-items:center;gap:16px}
.testimonials h2 em{font-style:normal;color:var(--red)}
.testimonials h2::after{content:"";flex:1;border-top:1px solid var(--line)}
.quotes{display:flex;gap:40px;margin-top:30px}
.quote{flex:1}
.bubble{border:1px solid var(--line);padding:18px 20px;font-size:12px;position:relative;height:110px}
.bubble::after{content:"";position:absolute;left:40px;bottom:-9px;width:16px;height:16px;background:var(--white);border-right:1px solid var(--line);border-bottom:1px solid var(--line);transform:rotate(45deg)}
.author{display:flex;align-items:center;gap:12px;margin-top:22px;padding-left:20px}
.avatar{width:46px;height:46px;border-radius:50%;background:#c9b7a6}
.author b{display:block;font-size:13px;font-weight:600}
.stars{color:var(--blue);font-size:12px;letter-spacing:1px}

/* footer */
.footer{position:absolute;left:0;top:2230px;width:1200px;height:230px;background:var(--footer);color:#cfd3d6;font-size:12px}
.footer .wrap{display:flex;gap:40px;padding-top:34px}
.f-col{flex:1}
.f-col.wide{flex:1.5}
.f-col h4{color:var(--red);font-size:11px;font-weight:700;margin-bottom:10px}
.f-col ul{list-style:none}
.f-col li{margin-bottom:3px}
.f-brand{display:flex;align-items:center;gap:8px;margin-bottom:14px}
.f-brand .brand-mark{width:30px;height:30px}
.f-brand .brand-name{color:var(--white);font-size:14px}
.news{display:flex;gap:10px;margin-bottom:12px}
.news .date{width:36px;height:36px;border:1px solid #cfd3d6;flex:none;text-align:center;font-size:10px;line-height:1.2;padding-top:5px;color:var(--white)}
.bottom{position:absolute;left:0;top:2460px;width:1200px;height:40px;background:var(--footer-deep);color:#aab;font-size:11px}
.bottom .wrap{display:flex;align-items:center;justify-content:space-between;height:40px}
.social{display:flex;gap:8px}
.social span{width:20px;height:20px;border-radius:50%;background:#cfd3d6}
</style>
</head>
<body>

<header>
  <div class="wrap topbar">
    <div class="brand"><span class="brand-mark"></span><span class="brand-name">TALL OAK BUILDING SERVICES</span></div>
    <div class="contact">
      <div><svg viewBox="0 0 16 16"><path d="M3 1l3 3-2 2c1 2 3 4 5 5l2-2 3 3-2 3C6 15 1 10 1 3z" fill="#333"/></svg>020 555 0148</div>
      <div><svg viewBox="0 0 16 16"><rect x="1" y="3" width="14" height="10" fill="none" stroke="#333" stroke-width="1.5"/><path d="M1 3l7 6 7-6" fill="none" stroke="#333" stroke-width="1.5"/></svg>info@talloakbuilders.com</div>
    </div>
  </div>
  <nav class="nav">
    <div class="wrap">
      <ul>
        <li class="active">HOME</li><li>SERVICES</li><li>GALLERY</li><li>TESTIMONIALS</li><li>ABOUT US</li><li>CONTACT US</li>
      </ul>
      <svg class="search" viewBox="0 0 16 16"><circle cx="6.5" cy="6.5" r="5" fill="none" stroke="#fff" stroke-width="2"/><path d="M10 10l5 5" stroke="#fff" stroke-width="2"/></svg>
    </div>
  </nav>
</header>

<section class="hero" role="img" aria-label="Photo of a stone-fronted family house with garden and flowering shrubs">
  <svg class="arrow prev" viewBox="0 0 28 28"><path d="M18 5L9 14l9 9" fill="none" stroke="#fff" stroke-width="2"/></svg>
  <svg class="arrow next" viewBox="0 0 28 28"><path d="M10 5l9 9-9 9" fill="none" stroke="#fff" stroke-width="2"/></svg>
  <div class="hero-quote">
    <h1>The home should be<br>the treasure chest of living.</h1>
    <p>A. Marlowe</p>
  </div>
  <div class="dots"><span class="on"></span><span></span><span></span><span></span></div>
</section>

<main class="wrap">
  <div class="services-head">
    <svg viewBox="0 0 16 16"><path d="M11 2L5 8l6 6" fill="none" stroke="#2a8fd8" stroke-width="2"/></svg>
    <h2 class="sec-title">Our <em>Services</em></h2>
    <svg viewBox="0 0 16 16"><path d="M5 2l6 6-6 6" fill="none" stroke="#d7212b" stroke-width="2"/></svg>
  </div>

  <div class="cards">
    <article class="card">
      <h3>Deck <em>Building</em></h3>
      <div class="photo" role="img" aria-label="Photo of a wooden deck with patio furniture" style="background:linear-gradient(135deg,#b9794a,#7a4a2c)"></div>
      <p>Lorem Ipsum is simply dummy text of the printing and typesetting industry. Lorem Ipsum has been the industry's standard dummy text ever since the 1500 Lorem Ipsum is simply dummy text of the printing and typesetting industry. Lorem Ipsum has been the industry's standard dummy text ever since the 1500 and typesetting industry.</p>
      <span class="more">MORE</span>
    </article>
    <article class="card">
      <h3>Replacement <em>Windows</em></h3>
      <div class="photo" role="img" aria-label="Photo of white windows with red flower boxes on a brick wall" style="background:linear-gradient(135deg,#a8614a,#6e3a2e)"></div>
      <p>Lorem Ipsum is simply dummy text of the printing and typesetting industry. Lorem Ipsum has been the industry's standard dummy text ever since the 1500 Lorem Ipsum is simply dummy text of the printing and typesetting industry. Lorem Ipsum has been the industry's standard dummy text ever since the 1500 and typesetting industry.</p>
      <span class="more">MORE</span>
    </article>
    <article class="card">
      <h3>Roofing <em>Work</em></h3>
      <div class="photo" role="img" aria-label="Photo of timber roof framing under construction" style="background:linear-gradient(135deg,#c9a27a,#8a6a4c)"></div>
      <p>Lorem Ipsum is simply dummy text of the printing and typesetting industry. Lorem Ipsum has been the industry's standard dummy text ever since the 1500 Lorem Ipsum is simply dummy text of the printing and typesetting industry. Lorem Ipsum has been the industry's standard dummy text ever since the 1500 and typesetting industry.</p>
      <span class="more">MORE</span>
    </article>
  </div>

  <section class="about">
    <h2 class="sec-title">About <em>Tall Oak Building Services</em></h2>
    <p>Lorem Ipsum is simply dummy text of the printing and typesetting industry. Lorem Ipsum has been the industry's standard dummy text ever since the 1500 Lorem Ipsum is simply dummy text of the printing and typesetting industry. Lorem Ipsum has been the industry's standard dummy text ever since the 1500 Lorem Ipsum is simply dummy text of the printing and typesetting industry. Lorem Ipsum has been the industry's standard dummy text ever since the 1500 Lorem Ipsum is simply dummy text of the printing and typesetting industry. Lorem Ipsum has been the industry's standard dummy text ever since the 1500 and typesetting industry.</p>
    <hr class="rule">
  </section>

  <section class="gallery">
    <h2 class="sec-title">Our <em>Photo Gallery</em></h2>
    <div class="gallery-row">
      <div role="img" aria-label="Photo of a modern apartment building under blue sky" style="background:linear-gradient(180deg,#6fa2d6,#b7b3aa)"></div>
      <div role="img" aria-label="Photo of a suburban house with garage" style="background:linear-gradient(180deg,#9fb6c8,#8b8577)"></div>
      <div role="img" aria-label="Photo of a red-roofed house with lawn" style="background:linear-gradient(180deg,#a9463a,#5d7a3c)"></div>
      <div role="img" aria-label="Photo of a large family home at dusk" style="background:linear-gradient(180deg,#7e8ea0,#6a5a44)"></div>
    </div>
  </section>

  <section class="testimonials">
    <h2>Happy Clients <em>Say its Amazig!</em></h2>
    <div class="quotes">
      <div class="quote">
        <div class="bubble">Lorem Ipsum is simply dummy text of the printing and typesetting industry. Lorem Ipsum has been the industry's.</div>
        <div class="author"><span class="avatar" role="img" aria-label="Client portrait"></span><div><b>Karen Holt</b><span class="stars">★★★★☆</span></div></div>
      </div>
      <div class="quote">
        <div class="bubble">Lorem Ipsum is simply dummy text of the printing and typesetting industry. Lorem Ipsum has been the industry's.</div>
        <div class="author"><span class="avatar" role="img" aria-label="Client portrait"></span><div><b>Irene Walsh</b><span class="stars">★★★★☆</span></div></div>
      </div>
      <div class="quote">
        <div class="bubble">Lorem Ipsum is simply dummy text of the printing and typesetting industry. Lorem Ipsum has been the industry's.</div>
        <div class="author"><span class="avatar" role="img" aria-label="Client portrait"></span><div><b>Simon Drake</b><span class="stars">★★★★☆</span></div></div>
      </div>
    </div>
  </section>
</main>

<footer class="footer">
  <div class="wrap">
    <div class="f-col wide">
      <div class="f-brand"><span class="brand-mark"></span><span class="brand-name">TALL OAK BUILDING SERVICES</span></div>
      <p>Lorem Ipsum is simply dummy text of the printing and typesetting industry. Lorem Ipsum has been the industry's.</p>
      <p style="margin-top:8px">Tel: 020 555 0148<br>email: info@talloakbuilders.com</p>
    </div>
    <div class="f-col">
      <h4>WHAT WE ARE</h4>
      <ul><li>About Us</li><li>Our Work</li><li>Blog</li><li>Contact Us</li></ul>
    </div>
    <div class="f-col">
      <h4>WHAT WE DO</h4>
      <ul><li>Deck Building</li><li>Replacement Windows</li><li>Roofing Work</li><li>Replacement Siding</li><li>In House Consultation</li></ul>
    </div>
    <div class="f-col wide">
      <h4>LATEST NEWS</h4>
      <div class="news"><span class="date">12<br>JUN</span><p>Lorem Ipsum is simply dummy text of the printing and typesetting.</p></div>
      <div class="news"><span class="date">04<br>JUN</span><p>Lorem Ipsum is simply dummy text of the printing and typesetting.</p></div>
    </div>
  </div>
</footer>
<div class="bottom">
  <div class="wrap">
    <span>Copyright © 2015 Tall Oak Building Services</span>
    <div class="social"><span></span><span></span><span></span><span></span></div>
    <span>Privacy Policy &nbsp;|&nbsp; Sitemap</span>
  </div>
</div>

</body>
</html>
```